Broschüre für eine Trainingsakademie
Zielgruppe
Ich möchte eine Broschüre zu meinem Unternehmen und meinen Angeboten schöner Design haben.
Ich bin Trainer/ Coach für moderne Personalstrategien insbesondere für die Personalgewinnung, Mitarbeiterbindung und -entwicklung. Zudem biete ich Trainings und Coachings für Mitarbeiter und Führungskräfte an. Zum Beispiel zu Themen wie gesunde Führung, Stressmanagement, Resilienz usw.
Meine Zielgruppe sind vor allem mittelständische Unternehmen oder junge aufstrebende StartUps, die ich beim Aufbau von Personalstrukturen unterstütze.
Aufgabenstellung
Mein Logo und die Farben sollen entsprechend berücksichtigt werden. Ein Entwurf für die Broschüre besteht bereits. Das ist allerdings nur meine Idee, als Laie. Ich hätte hier gern professionelle Ideen, so dass die Broschüre professionell und ansprechend wirkt.
Bilder habe ich eigentlich - diese finden sich auch auf meiner Homepage. Allerdings bin ich gerade auch beim Deckblatt offen. Auch für andere Gestaltungsvorschläge.

```html
<!DOCTYPE html>
<html lang="de">
<head>
<meta charset="utf-8">
<title>Halvorsen Coaching – Broschüre</title>
<link href="https://fonts.googleapis.com/css2?family=Roboto:wght@300;400;500&display=swap" rel="stylesheet">
<style>
  :root {
    --bg: #f1f0f4;
    --paper: #ffffff;
    --ink: #1e1d22;
    --brand: #5b4a86;
    --lavender: #9d97b5;
    --lavender-soft: #d9d6e4;
    --pagenum: #a29eb6;
    --teal: #8fd0cc;
  }
  * { box-sizing: border-box; margin: 0; padding: 0; }
  html, body { width: 1200px; height: 600px; overflow: hidden; }
  body {
    background: var(--bg);
    font-family: "Roboto", Arial, sans-serif;
    color: var(--ink);
    position: relative;
  }
  .page {
    position: absolute;
    width: 387px;
    height: 272px;
    background: var(--paper);
    border: 1px solid #2a2830;
    overflow: hidden;
  }
  .page--5 { left: 39px; top: 27px; }
  .page--6 { left: 405px; top: 163px; }
  .page--7 { left: 770px; top: 299px; }

  .corner-bands { position: absolute; left: 0; top: 0; width: 140px; height: 130px; }

  .brand-name {
    position: absolute;
    width: 80px;
    text-align: center;
    color: var(--brand);
    font-weight: 500;
    line-height: 1;
  }
  .brand-name__main { display: block; font-size: 11px; letter-spacing: 0.6px; }
  .brand-name__sub { display: block; font-size: 4px; letter-spacing: 0.8px; margin-top: 1px; }

  .copy {
    position: absolute;
    font-size: 6.6px;
    line-height: 9.1px;
    text-align: justify;
    word-spacing: 1px;
  }
  .copy--intro { font-weight: 500; }

  .bulb { position: absolute; width: 13px; height: 13px; }

  .rule-h { position: absolute; height: 1px; background: var(--brand); }
  .rule-v { position: absolute; width: 1px; background: var(--brand); }

  .section-title {
    position: absolute;
    left: 28px;
    top: 212px;
    font-size: 8.6px;
    white-space: nowrap;
  }
  .section-title b { font-weight: 500; }
  .section-title .light { font-weight: 300; font-size: 7.2px; margin: 0 3px; }
  .section-title .big { font-weight: 400; font-size: 10.8px; }

  .page-number {
    position: absolute;
    top: 249px;
    width: 14px;
    height: 23px;
    background: var(--pagenum);
    color: #fff;
    font-size: 9px;
    font-weight: 300;
    text-align: center;
    padding-top: 5px;
  }

  .artwork { position: absolute; }
  .artwork--ladder { left: 339px; top: 194px; width: 39px; height: 78px; background: linear-gradient(180deg, #d7d4e1, #8c87a3); }
  .artwork--hero { left: 219px; top: 71px; width: 168px; height: 113px; background: var(--lavender); }
  .artwork--signpost { left: 313px; top: 196px; width: 44px; height: 76px; background: linear-gradient(180deg, #ece9f3, #cfcbdd); }
  .artwork--maze { left: 281px; top: 145px; width: 80px; height: 57px; background: linear-gradient(135deg, var(--brand) 40%, var(--teal)); }

  .strategy-heading {
    position: absolute;
    left: 28px;
    top: 23px;
    font-size: 11.4px;
    font-weight: 300;
    letter-spacing: 0.2px;
  }
  .strategy-heading b { font-weight: 500; }
  .connector { position: absolute; left: 0; top: 0; width: 387px; height: 272px; }

  .bullet-list {
    position: absolute;
    left: 28px;
    top: 45px;
    width: 158px;
    list-style: none;
    font-size: 6.6px;
    line-height: 9.1px;
  }
  .bullet-list li { position: relative; padding-left: 6px; text-align: justify; }
  .bullet-list li::before { content: "•"; position: absolute; left: 0; color: var(--brand); }

  .offer-title {
    position: absolute;
    left: 28px;
    top: 212px;
    font-size: 10.6px;
    font-weight: 300;
  }
  .offer-title b { font-weight: 500; }
</style>
</head>
<body>

<!-- Seite 5 -->
<section class="page page--5">
  <svg class="corner-bands" viewBox="0 0 140 130" aria-hidden="true">
    <polygon points="14,0 30,0 120,90 104,106" fill="var(--lavender-soft)" opacity="0.7"/>
    <polygon points="0,20 0,44 80,124 100,110" fill="var(--lavender-soft)" opacity="0.45"/>
    <polygon points="22,0 30,0 60,30 52,38" fill="#ffffff"/>
  </svg>

  <p class="copy copy--intro" style="left:28px; top:26px; width:151px;">Damit die Trainings und Coachings wirklich in der Praxis umgesetzt werden und einen langfristigen Mehrwert bieten:</p>

  <div class="brand-name" style="left:279px; top:27px;">
    <span class="brand-name__main">HALVORSEN</span>
    <span class="brand-name__sub">COACHING</span>
  </div>

  <svg class="bulb" style="left:24px; top:63px;" viewBox="0 0 13 13" aria-hidden="true">
    <g stroke="#6c6780" stroke-width="0.6"><line x1="6.5" y1="0" x2="6.5" y2="2"/><line x1="1" y1="2" x2="2.6" y2="3.4"/><line x1="12" y1="2" x2="10.4" y2="3.4"/><line x1="0" y1="6" x2="2" y2="6"/><line x1="11" y1="6" x2="13" y2="6"/></g>
    <circle cx="6.5" cy="6" r="2.6" fill="#5b5670"/><rect x="5.2" y="8.4" width="2.6" height="3" fill="#5b5670"/>
  </svg>
  <p class="copy" style="left:28px; top:71px; width:146px;">&nbsp;&nbsp;&nbsp;&nbsp;Training aus der Praxis für die Praxis: Über 12 Jahre relevante Berufserfahrung im Personalwesen/ in der Personalleitung in internationalen renommierten Unternehmen, Führungserfahrung und die Leitung eines Profit Centers im Handel bilden das Rüstzeug für Halvorsen Coaching. Ihre Probleme des Alltags kenne ich nicht nur aus der Theorie, sondern aus dem eigenen Berufsleben!</p>

  <svg class="bulb" style="left:202px; top:63px;" viewBox="0 0 13 13" aria-hidden="true">
    <g stroke="#6c6780" stroke-width="0.6"><line x1="6.5" y1="0" x2="6.5" y2="2"/><line x1="1" y1="2" x2="2.6" y2="3.4"/><line x1="12" y1="2" x2="10.4" y2="3.4"/><line x1="0" y1="6" x2="2" y2="6"/><line x1="11" y1="6" x2="13" y2="6"/></g>
    <circle cx="6.5" cy="6" r="2.6" fill="#5b5670"/><rect x="5.2" y="8.4" width="2.6" height="3" fill="#5b5670"/>
  </svg>
  <p class="copy" style="left:206px; top:71px; width:151px;">&nbsp;&nbsp;&nbsp;Methoden mit System: In den Trainings und Coachings wird mit wissenschaftlich erprobten Methoden, Tests und Konzepten gearbeitet. Die Eignungsdiagnostik orientiert sich an den Anforderungen der DIN 33430 und wendet Tests an, die diesen Kriterien entsprechen. Coaching Ausbildungen in den Bereichen Business Coaching, Hypnose Coaching, NLP, Stress- und Mentalcoaching bieten eine große Varianz an Trainingsmethoden, die je nach den jeweiligen Anforderungen situationsgerecht und effektiv angewendet werden.</p>

  <div class="rule-h" style="left:0; top:206px; width:205px;"></div>
  <div class="rule-v" style="left:19px; top:194px; height:56px;"></div>
  <h2 class="section-title"><b>Trainings</b><span class="light">und</span><b>Coachings</b><span class="light">mit</span><span class="big">Mehrwert</span></h2>

  <div class="artwork artwork--ladder" role="img" aria-label="Illustration: Figur, die eine Leiter hinaufsteigt"></div>
  <div class="page-number" style="left:343px;">5</div>
</section>

<!-- Seite 6 -->
<section class="page page--6">
  <svg class="corner-bands" viewBox="0 0 140 130" aria-hidden="true">
    <polygon points="14,0 30,0 120,90 104,106" fill="var(--lavender-soft)" opacity="0.7"/>
    <polygon points="0,20 0,44 80,124 100,110" fill="var(--lavender-soft)" opacity="0.45"/>
    <polygon points="22,0 30,0 60,30 52,38" fill="#ffffff"/>
  </svg>

  <div class="brand-name" style="left:278px; top:27px;">
    <span class="brand-name__main">HALVORSEN</span>
    <span class="brand-name__sub">COACHING</span>
  </div>

  <svg class="bulb" style="left:27px; top:64px;" viewBox="0 0 13 13" aria-hidden="true">
    <g stroke="#6c6780" stroke-width="0.6"><line x1="6.5" y1="0" x2="6.5" y2="2"/><line x1="1" y1="2" x2="2.6" y2="3.4"/><line x1="12" y1="2" x2="10.4" y2="3.4"/><line x1="0" y1="6" x2="2" y2="6"/><line x1="11" y1="6" x2="13" y2="6"/></g>
    <circle cx="6.5" cy="6" r="2.6" fill="#5b5670"/><rect x="5.2" y="8.4" width="2.6" height="3" fill="#5b5670"/>
  </svg>
  <p class="copy" style="left:29px; top:72px; width:146px;">&nbsp;&nbsp;&nbsp;&nbsp;Begleitung in die Praxis: Viele gute Seminare verlieren Ihre Wirkung, weil die gewonnenen Erkenntnisse und Inhalte in ihrem persönlichen Berufsalltag nicht umgesetzt werden können. Meine Personal-Erfolgs-Strategie beinhaltet deshalb immer ein passgenaues und zielgerichtetes Coaching/ Training sowie eine gezielte Umsetzungsbegleitung. Diese schließt neben den eigentlichen Seminar-Teilnehmern auch die Vorgesetzten und/oder Personalabteilung ein, um die Praxisumsetzung gezielt zu begleiten und zu unterstützen.</p>

  <svg class="bulb" style="left:204px; top:63px;" viewBox="0 0 13 13" aria-hidden="true">
    <g stroke="#6c6780" stroke-width="0.6"><line x1="6.5" y1="0" x2="6.5" y2="2"/><line x1="1" y1="2" x2="2.6" y2="3.4"/><line x1="12" y1="2" x2="10.4" y2="3.4"/><line x1="0" y1="6" x2="2" y2="6"/><line x1="11" y1="6" x2="13" y2="6"/></g>
    <circle cx="6.5" cy="6" r="2.6" fill="#5b5670"/><rect x="5.2" y="8.4" width="2.6" height="3" fill="#5b5670"/>
  </svg>
  <div class="artwork artwork--hero" role="img" aria-label="Illustration: Geschäftsmann mit Umhang und erhobener Faust zwischen Wolken"></div>

  <div class="rule-h" style="left:0; top:206px; width:205px;"></div>
  <div class="rule-v" style="left:19px; top:194px; height:56px;"></div>
  <h2 class="section-title"><b>Trainings</b><span class="light">und</span><b>Coachings</b><span class="light">mit</span><span class="big">Mehrwert</span></h2>

  <div class="artwork artwork--signpost" role="img" aria-label="Illustration: Wegweiser mit mehreren Richtungsschildern"></div>
  <div class="page-number" style="left:343px;">6</div>
</section>

<!-- Seite 7 -->
<section class="page page--7">
  <svg class="corner-bands" viewBox="0 0 140 130" aria-hidden="true">
    <polygon points="14,0 30,0 80,50 64,66" fill="var(--lavender-soft)" opacity="0.7"/>
    <polygon points="0,14 0,34 40,74 56,60" fill="var(--lavender-soft)" opacity="0.45"/>
  </svg>

  <h2 class="strategy-heading">PERSONAL<b>STRATEGIE</b></h2>
  <svg class="connector" viewBox="0 0 387 272" aria-hidden="true">
    <polyline points="154,30 219,30 219,153 279,153" fill="none" stroke="#4a4658" stroke-width="0.8" stroke-dasharray="1 1.4"/>
  </svg>

  <div class="brand-name" style="left:282px; top:26px;">
    <span class="brand-name__main">HALVORSEN</span>
    <span class="brand-name__sub">COACHING</span>
  </div>

  <ul class="bullet-list">
    <li>Strategische Personalauswahl: Von der richtigen Anforderungsanalyse über die Ausschreibung zum Bewerbungs- und Auswahlprozesses bis zum gelungenen Onboarding - ausgerichtet auf Ihr Employer Branding.</li>
    <li>Eignungsdiagnostik: Von der Auswahl einzelner Tests bis zur Konzeption und Begleitung von Bewerbertagen ausgerichtet auf die jeweilige Stellenanforderung.</li>
    <li>Strategische Mitarbeiterplanung und -bindung: Entwicklung von Strukturen zur Mitarbeiterbindung und -entwicklung auch im Hinblick auf Personalkennzahlen.</li>
  </ul>

  <div class="artwork artwork--maze" role="img" aria-label="Illustration: Menschen auf verschlungenen Wegen in einem Labyrinth"></div>

  <div class="rule-h" style="left:0; top:205px; width:387px;"></div>
  <div class="rule-v" style="left:19px; top:193px; height:55px;"></div>
  <h2 class="offer-title">Trainings<b>angebot</b></h2>

  <div class="page-number" style="left:346px;">7</div>
</section>

</body>
</html>
```